High end business card design for custom homebuilding company

Looking for a high end business card design that is unique and elegant. Can use embossing, foil printing, laser die cutting, or any high end printing technique or high end paper. Will upload current design so you can see the logo and what we are using currently, but we want something more unique and elegant. I included our logo to help with design.

Target Market(s)

High end custom home buyers of $1.5 million plus homes. Also real estate developers of high end communities.

Industry/Entity Type

Business

Contact Information for Business Card

Double sided. We want something very elegant and expensive looking. We are looking to incorporate a combination of perhaps linen paper or a high end paper, with foil stamping or embossing/debossing to make the card look unique, but still elegant. We tend to use blacks and golds, but are open to any ideas. Looking for creative and unique design.

Colors

Designer to choose colors to be used in the design.

Requirements
Must have
• High end, elegant look. Can use foil, embossing, or high end papers like linen. We want to make the card unique and interesting, but elegant and expensive looking.
Nice to have
• I am including just some cards I saw that looked interesting for one reason or another. I like a clean elegant design and like both the clean white style, and the blacks. So not sure if we want a black design or white. Would like to see both.

```html
<!DOCTYPE html>
<html lang="en">
<head>
<meta charset="utf-8">
<title>Highmark Custom Homes – Business Card</title>
<link rel="stylesheet" href="https://fonts.googleapis.com/css2?family=Crimson+Pro:wght@600&display=swap">
<style>
  :root {
    --bg: #f3f3f1;
    --card: #2a2a2a;
    --gold: #d8a757;
    --shadow: rgba(0, 0, 0, 0.28);
  }
  * { margin: 0; padding: 0; box-sizing: border-box; }
  html, body {
    width: 1200px; height: 1000px; overflow: hidden;
    background: var(--bg);
    font-family: "Crimson Pro", Georgia, serif;
    font-weight: 600;
    color: var(--gold);
  }
  .canvas { position: relative; width: 1200px; height: 1000px; }
  .card {
    position: absolute;
    width: 573px; height: 352px;
    background: var(--card);
    box-shadow: 1px 3px 4px var(--shadow);
  }
  .card--front { left: 293px; top: 132px; }
  .card--back  { left: 294px; top: 519px; }

  .brand {
    position: absolute;
    display: flex; align-items: center; gap: 10px;
    white-space: nowrap;
  }
  .brand__dot { border-radius: 50%; background: var(--gold); flex: none; }
  .brand__name { text-transform: uppercase; letter-spacing: 0.08em; }

  .card--front .brand { left: 50%; top: 50%; transform: translate(-50%, -50%); }
  .card--front .brand__dot { width: 34px; height: 34px; }
  .card--front .brand__name { font-size: 30px; }

  .card--back .brand { right: 37px; top: 40px; gap: 6px; }
  .card--back .brand__dot { width: 16px; height: 16px; }
  .card--back .brand__name { font-size: 14px; }

  .person {
    position: absolute; left: 38px; top: 92px;
    font-size: 16px; letter-spacing: 0.2em;
  }
  .person__rule {
    position: absolute; left: 39px; top: 122px;
    width: 32px; height: 3px; background: var(--gold);
  }
  .contact { position: absolute; left: 36px; top: 152px; list-style: none; }
  .contact__item {
    display: flex; align-items: flex-start; gap: 13px;
    font-size: 12.5px; letter-spacing: 0.08em; line-height: 19px;
    margin-bottom: 16px;
  }
  .contact__item svg { flex: none; width: 13px; height: 13px; margin-top: 3px; fill: var(--gold); }

  .social {
    position: absolute; right: 37px; top: 230px;
    text-align: right;
  }
  .social__label { font-size: 12px; letter-spacing: 0.12em; }
  .social__list { display: flex; justify-content: flex-end; gap: 4px; margin-top: 14px; }
  .social__dot { width: 24px; height: 24px; border-radius: 50%; background: var(--gold); }
  .website {
    position: absolute; right: 37px; top: 294px;
    font-size: 11.5px; letter-spacing: 0.12em;
  }
</style>
</head>
<body>
<main class="canvas">
  <section class="card card--front">
    <div class="brand">
      <span class="brand__dot"></span>
      <span class="brand__name">Highmark Custom Homes</span>
    </div>
  </section>

  <section class="card card--back">
    <div class="brand">
      <span class="brand__dot"></span>
      <span class="brand__name">Highmark Custom Homes</span>
    </div>

    <p class="person">DUMMY NAME</p>
    <span class="person__rule"></span>

    <ul class="contact">
      <li class="contact__item">
        <svg viewBox="0 0 24 24"><path d="M6.6 10.8a15.1 15.1 0 0 0 6.6 6.6l2.2-2.2a1 1 0 0 1 1-.25 11.4 11.4 0 0 0 3.6.57 1 1 0 0 1 1 1V20a1 1 0 0 1-1 1A17 17 0 0 1 3 4a1 1 0 0 1 1-1h3.5a1 1 0 0 1 1 1c0 1.25.2 2.45.57 3.57a1 1 0 0 1-.25 1z"/></svg>
        <span>Dummy Phone</span>
      </li>
      <li class="contact__item">
        <svg viewBox="0 0 24 24"><path d="M2 5h20v14H2z M3.5 6.5 12 13l8.5-6.5v1.8L12 14.8 3.5 8.3z" fill-rule="evenodd"/></svg>
        <span>Dummy@info.com.au</span>
      </li>
      <li class="contact__item">
        <svg viewBox="0 0 24 24"><path d="M12 2a7 7 0 0 0-7 7c0 5.2 7 13 7 13s7-7.8 7-13a7 7 0 0 0-7-7zm0 9.5A2.5 2.5 0 1 1 12 6.5a2.5 2.5 0 0 1 0 5z"/></svg>
        <span>Unit 3 14-18 Ashford Lane,<br>Bayview, WA 6100</span>
      </li>
    </ul>

    <div class="social">
      <p class="social__label">follow us on:</p>
      <div class="social__list">
        <span class="social__dot"></span>
        <span class="social__dot"></span>
        <span class="social__dot"></span>
        <span class="social__dot"></span>
        <span class="social__dot"></span>
      </div>
    </div>
    <p class="website">www.highmarkcustomhomes.com.au</p>
  </section>
</main>
</body>
</html>
```